Quillfern Rise A4 Potrait foldout brochure

We need a brochure design for this residential land development. I have attached the a style that we like to base our design on. Full colour required. will provide files required for design also. PLEASE DO NOT COPY THIS DESIGN. Come up with a new style that gives you this feeling. Please note the plan needs to be positioned landscape on the inside 2 A4 Pages.

Industry/Entity Type

Residential

Font styles to use
Other font styles liked:
• Try with Century Gothich

Requirements
Must have
• use same colours as supplied in Quillfern rise brochure.
Nice to have
• nice modern simple background graphics

```html
<!DOCTYPE html>
<html lang="en">
<head>
<meta charset="utf-8">
<title>Quillfern Rise – Masterplan Brochure</title>
<link rel="stylesheet" href="https://fonts.googleapis.com/css2?family=Questrial&family=Open+Sans:wght@600;700&display=swap">
<style>
  :root {
    --stage: #dcdcdc;
    --forest: #064a1f;
    --leaf: #6cc24a;
    --grass: #3f9a35;
    --meadow: #2f8a2a;
    --sun: #f7b81c;
    --violet: #7b2f8e;
    --paper: #ffffff;
    --road: #2b2b2b;
    --ink: #1c1c1c;
  }
  * { box-sizing: border-box; margin: 0; padding: 0; }
  html, body { width: 1200px; height: 1068px; overflow: hidden; }
  body { background: var(--stage); position: relative; font-family: "Questrial", sans-serif; }

  .page { position: absolute; width: 360px; height: 509px; overflow: hidden; box-shadow: 0 6px 18px rgba(0,0,0,.18); }

  .pattern-band {
    position: absolute; left: 0; right: 0;
    background: linear-gradient(100deg, var(--leaf) 0%, var(--sun) 22%, var(--violet) 38%, var(--grass) 55%, var(--sun) 72%, var(--violet) 88%, var(--leaf) 100%);
  }

  /* Cover */
  .cover { left: 36px; top: 280px; background: var(--forest); }
  .cover .pattern-band.top { top: 0; height: 82px; clip-path: polygon(0 0,100% 0,100% 100%,78% 70%,55% 92%,30% 62%,12% 80%,0 70%); }
  .cover .pattern-band.bottom { bottom: 0; height: 92px; clip-path: polygon(0 20%,18% 40%,40% 28%,62% 52%,82% 44%,100% 60%,100% 100%,0 100%); }
  .brand { position: absolute; left: 0; right: 0; top: 188px; text-align: center; white-space: nowrap; }
  .brand-mark { display: inline-block; width: 14px; height: 14px; border-radius: 50%; background: var(--paper); margin-right: 8px; vertical-align: middle; }
  .brand-name { font-size: 34px; color: var(--paper); vertical-align: middle; letter-spacing: .5px; }
  .cover-title { position: absolute; left: 0; right: 0; top: 266px; text-align: center; font-size: 38px; font-weight: 400; color: var(--leaf); letter-spacing: 1px; }

  /* Inside spread */
  .spread { left: 444px; top: 280px; width: 720px; background: var(--paper); }
  .spread .fold { position: absolute; left: 360px; top: 0; bottom: 0; width: 1px; background: rgba(0,0,0,.08); }
  .spread .pattern-band.top { top: 0; height: 38px; clip-path: polygon(0 0,100% 0,100% 100%,85% 40%,70% 80%,52% 30%,35% 70%,18% 35%,0 75%); }
  .spread .pattern-band.bottom { bottom: 0; left: 360px; height: 46px; clip-path: polygon(0 60%,20% 20%,40% 55%,60% 15%,80% 50%,100% 0,100% 100%,0 100%); }
  .site-plan {
    position: absolute; left: 28px; top: 56px; width: 664px; height: 290px;
    border: 10px solid var(--road);
    background:
      radial-gradient(ellipse at 30% 70%, rgba(6,74,31,.35), transparent 55%),
      radial-gradient(ellipse at 75% 30%, rgba(108,194,74,.45), transparent 60%),
      linear-gradient(160deg, #55ad3d 0%, var(--meadow) 50%, #3b9a33 80%, #2a2a2a 100%);
  }
  .lot-legend { position: absolute; left: 40px; top: 366px; list-style: none; font-family: "Open Sans", sans-serif; font-weight: 700; font-size: 12px; color: var(--ink); }
  .lot-legend li { display: flex; align-items: center; gap: 10px; margin-bottom: 8px; }
  .legend-key { width: 16px; height: 16px; flex: none; }
  .legend-key.stage-one { background: var(--grass); }
  .legend-key.stage-two { background: var(--sun); }
  .spread-brand { position: absolute; right: 40px; bottom: 72px; white-space: nowrap; }
  .spread-brand .brand-mark { background: var(--forest); width: 12px; height: 12px; }
  .spread-brand .brand-name { color: var(--forest); font-size: 26px; }
</style>
</head>
<body>
  <section class="page cover">
    <div class="pattern-band top" role="img" aria-label="Geometric triangle pattern in green, yellow and purple"></div>
    <div class="brand"><span class="brand-mark"></span><span class="brand-name">Quillfern Rise</span></div>
    <h1 class="cover-title">Masterplan</h1>
    <div class="pattern-band bottom" role="img" aria-label="Geometric triangle pattern in green, yellow and purple"></div>
  </section>

  <section class="page spread">
    <div class="pattern-band top" role="img" aria-label="Geometric triangle pattern in green, yellow and purple"></div>
    <div class="fold"></div>
    <div class="site-plan" role="img" aria-label="Subdivision masterplan: 47 numbered residential lots with their areas in square metres, laid out along three roads, with a large reserve lot and pond"></div>
    <ul class="lot-legend">
      <li><span class="legend-key stage-one"></span>Lots 1, 2, 13 to 16 &amp; 27 to 47.</li>
      <li><span class="legend-key stage-two"></span>Lots 3 to 12 &amp; 17 to 26.</li>
    </ul>
    <div class="spread-brand"><span class="brand-mark"></span><span class="brand-name">Quillfern Rise</span></div>
    <div class="pattern-band bottom" role="img" aria-label="Geometric triangle pattern in green, yellow and purple"></div>
  </section>
</body>
</html>
```